Rimah Advertising & Publicity business cards

I would like my Company's business card to be designed creatively & profissionally the logo is attached in both Arabic & english and prefer to have my emblem dimmed on the card as well
-Logo ( Arabic & English)
-Name (Arabic & English)
-Title ( Arabic & English)
-----------
-Location
-Landline (icon)
-Mobile phone (icon)
-Email (icon)
-Instagram (icon)
-WhatsApp (icon)

Target Market(s)

Industry/Entity Type

Marketing

Contact Information for Business Card

-Logo ( Arabic & English)
-Name (Arabic & English)
-----------
-Location
-Landline (icon)
-Mobile phone (icon)
-Email (icon)
-Instagram (icon)
-WhatsApp (icon)

Font styles to use
Serif

Requirements
Must have
• all what is mentions in business card details blanked and i will add the data my self
Nice to have
• Dim emblem on my business card both Arabic & english

```html
<!DOCTYPE html>
<html lang="en">
<head>
<meta charset="utf-8">
<title>Rimah Advertising &amp; Publicity – Business Cards</title>
<link href="https://fonts.googleapis.com/css2?family=Amiri:wght@400;700&family=Playfair+Display:wght@400&family=Raleway:wght@300&display=swap" rel="stylesheet">
<style>
  :root {
    --teal: #2cc4c4;
    --teal-soft: #bdeeed;
    --teal-faint: #e3f8f7;
    --card: #ffffff;
    --card-edge: #e9ebec;
    --ink: #1a1a1a;
    --backdrop: #3b3f47;
    --icon: #ffffff;
  }
  * { box-sizing: border-box; margin: 0; padding: 0; }
  html, body { width: 1200px; height: 800px; overflow: hidden; }
  body {
    background: var(--backdrop);
    position: relative;
    font-family: "Raleway", Arial, sans-serif;
  }
  .business-card {
    position: absolute;
    top: 240px;
    width: 540px;
    height: 320px;
    background: linear-gradient(135deg, var(--card) 55%, var(--card-edge) 100%);
    overflow: hidden;
    border-radius: 2px;
  }
  .business-card--arabic { left: 30px; }
  .business-card--english { left: 630px; }

  .corner-square {
    position: absolute;
    top: 0;
    left: 92px;
    width: 34px;
    height: 28px;
    background: var(--teal);
  }
  .contact-band {
    position: absolute;
    left: 92px;
    top: 120px;
    bottom: 0;
    width: 34px;
    background: var(--teal);
    display: flex;
    flex-direction: column;
    align-items: center;
    gap: 12px;
    padding-top: 12px;
  }
  .contact-band svg { width: 16px; height: 16px; display: block; }

  .brand {
    position: absolute;
    top: 40px;
    left: 150px;
    display: flex;
    align-items: center;
    gap: 16px;
  }
  .brand-mark {
    width: 64px;
    height: 64px;
    background: var(--teal);
    border-radius: 6px;
  }
  .brand-divider {
    width: 1px;
    height: 70px;
    background: var(--ink);
  }
  .brand-name {
    color: var(--ink);
    line-height: 1;
  }
  .brand-name--en {
    font-family: "Playfair Display", Georgia, serif;
    font-size: 54px;
    font-weight: 400;
  }
  .brand-tagline--en {
    font-family: "Raleway", Arial, sans-serif;
    font-weight: 300;
    font-size: 14px;
    color: var(--ink);
    margin-top: 6px;
    letter-spacing: 0.5px;
  }
  .brand-name--ar {
    font-family: "Amiri", "Times New Roman", serif;
    font-size: 56px;
    font-weight: 700;
    direction: rtl;
    text-align: right;
  }
  .brand-tagline--ar {
    font-family: "Amiri", "Times New Roman", serif;
    font-size: 16px;
    color: var(--ink);
    direction: rtl;
    text-align: right;
    margin-top: 2px;
  }
  .dimmed-emblem {
    position: absolute;
    right: 40px;
    bottom: -60px;
    width: 260px;
    height: 260px;
    border-radius: 50%;
    background: radial-gradient(circle, var(--teal-faint) 0%, var(--teal-soft) 100%);
    opacity: 0.75;
  }
</style>
</head>
<body>

<!-- Arabic face -->
<section class="business-card business-card--arabic" lang="ar">
  <div class="corner-square"></div>
  <div class="dimmed-emblem" role="img" aria-label="Dimmed company emblem area"></div>
  <div class="brand">
    <div class="brand-text">
      <div class="brand-name brand-name--ar">ريماه</div>
      <div class="brand-tagline--ar">للدعاية والإعلان</div>
    </div>
    <div class="brand-divider"></div>
    <div class="brand-mark" role="img" aria-label="Company emblem area"></div>
  </div>
  <div class="contact-band" aria-label="Contact icons">
    <svg viewBox="0 0 16 16" aria-label="Location"><path d="M8 2 L15 8 H13 V14 H3 V8 H1 Z" fill="var(--icon)"/></svg>
    <svg viewBox="0 0 16 16" aria-label="Landline"><rect x="2" y="5" width="12" height="9" rx="1" fill="var(--icon)"/><rect x="4" y="2" width="8" height="3" fill="var(--icon)"/></svg>
    <svg viewBox="0 0 16 16" aria-label="Mobile"><path d="M4 2 h3 l1 3 -2 1 q1 3 4 4 l1 -2 3 1 v3 q-1 2 -3 2 Q3 13 2 4 q0 -2 2 -2z" fill="var(--icon)"/></svg>
    <svg viewBox="0 0 16 16" aria-label="Email"><rect x="1" y="3" width="14" height="10" fill="var(--icon)"/><path d="M1 3 L8 9 L15 3" stroke="var(--teal)" stroke-width="1.2" fill="none"/></svg>
    <svg viewBox="0 0 16 16" aria-label="Photo sharing account"><rect x="2" y="2" width="12" height="12" rx="2" fill="var(--icon)"/></svg>
    <svg viewBox="0 0 16 16" aria-label="Messaging number"><circle cx="8" cy="8" r="6.5" fill="var(--icon)"/></svg>
  </div>
</section>

<!-- English face -->
<section class="business-card business-card--english" lang="en">
  <div class="corner-square"></div>
  <div class="dimmed-emblem" role="img" aria-label="Dimmed company emblem area"></div>
  <div class="brand">
    <div class="brand-mark" role="img" aria-label="Company emblem area"></div>
    <div class="brand-divider"></div>
    <div class="brand-text">
      <div class="brand-name brand-name--en">Rimah</div>
      <div class="brand-tagline--en">Advertising and Publicity</div>
    </div>
  </div>
  <div class="contact-band" aria-label="Contact icons">
    <svg viewBox="0 0 16 16" aria-label="Location"><path d="M8 2 L15 8 H13 V14 H3 V8 H1 Z" fill="var(--icon)"/></svg>
    <svg viewBox="0 0 16 16" aria-label="Landline"><rect x="2" y="5" width="12" height="9" rx="1" fill="var(--icon)"/><rect x="4" y="2" width="8" height="3" fill="var(--icon)"/></svg>
    <svg viewBox="0 0 16 16" aria-label="Mobile"><path d="M4 2 h3 l1 3 -2 1 q1 3 4 4 l1 -2 3 1 v3 q-1 2 -3 2 Q3 13 2 4 q0 -2 2 -2z" fill="var(--icon)"/></svg>
    <svg viewBox="0 0 16 16" aria-label="Email"><rect x="1" y="3" width="14" height="10" fill="var(--icon)"/><path d="M1 3 L8 9 L15 3" stroke="var(--teal)" stroke-width="1.2" fill="none"/></svg>
    <svg viewBox="0 0 16 16" aria-label="Photo sharing account"><rect x="2" y="2" width="12" height="12" rx="2" fill="var(--icon)"/></svg>
    <svg viewBox="0 0 16 16" aria-label="Messaging number"><circle cx="8" cy="8" r="6.5" fill="var(--icon)"/></svg>
  </div>
</section>

</body>
</html>
```